Halvick Ledgers & Advisory Tri-Fold Brochure (8.5"x11")

I need a professional looking brochure for my bookkeeping business. I am looking for something professional yet casual (not too corporate looking). I have attached a sample brochure that will outline the areas and a copy of our logo. I'd like to stick with shades of blue. The final product should communicate professional and personal.

Target Market(s)

Small service businesses.

Industry/Entity Type

Business

Font styles to use
Sans Serif

Requirements
Must have
• Professional looking photos of people in areas where it asks for a picture.

```html
<!DOCTYPE html>
<html lang="en">
<head>
<meta charset="utf-8">
<title>Halvick Ledgers &amp; Advisory – Tri-Fold Brochure (Inside)</title>
<link rel="stylesheet" href="https://fonts.googleapis.com/css2?family=Noto+Serif:wght@400&family=Tinos:wght@400&display=swap">
<style>
  :root {
    --backdrop: #b9d2e4;
    --paper: #f7f7f8;
    --band: #2a9fdc;
    --band-deep: #1f8fcf;
    --accent: #2a9ed8;
    --ink: #1b1b1b;
    --rule: #143a5a;
    --photo-light: #dfe7ef;
    --photo-mid: #9fb6cc;
    --photo-dark: #4d6781;
    --heading-font: "Noto Serif", Georgia, serif;
    --body-font: "Tinos", "Times New Roman", serif;
  }
  * { box-sizing: border-box; margin: 0; padding: 0; }
  html, body { width: 1200px; height: 913px; overflow: hidden; }
  body { background: var(--backdrop); position: relative; font-family: var(--body-font); color: var(--ink); }

  .brochure {
    position: absolute; left: 20px; top: 8px; width: 1160px; height: 896px;
    background: var(--paper); display: flex;
  }
  .panel { position: relative; width: 386.67px; height: 100%; overflow: hidden; }
  .panel + .panel { border-left: 1px solid #e2e4e7; }

  .photo {
    position: absolute; top: 0; height: 250px;
    background: linear-gradient(135deg, var(--photo-dark) 0%, var(--photo-mid) 30%, var(--photo-light) 60%, var(--photo-mid) 100%);
  }
  .band { position: absolute; background: var(--band); }

  /* Panel 1 */
  .panel--services .photo { left: 0; width: 100%; }
  .panel--services .band { top: 250px; left: 0; width: 100%; height: 22px; border-top: 4px solid var(--rule); }

  .panel-title { font-family: var(--heading-font); font-size: 28px; font-weight: 400; color: var(--ink); }
  .panel-title small { font-size: 14px; }

  .service { margin-top: 16px; }
  .service-head { display: flex; align-items: flex-start; gap: 12px; }
  .service-head h3 {
    font-family: var(--heading-font); font-weight: 400; font-size: 22px; line-height: 1.2; color: var(--accent);
  }
  .service-icon { flex: none; width: 28px; height: 28px; margin-top: 1px; }
  .service p { font-size: 15.5px; line-height: 1.08; text-align: justify; margin-top: 10px; }

  .services-col { position: absolute; left: 26px; right: 22px; top: 296px; }

  /* Panel 2 */
  .panel--why .photo { left: 0; width: 136px; }
  .panel--why .band--under-photo { top: 250px; left: 0; width: 136px; height: 80px; }
  .panel--why .band--foot { left: 0; right: 0; top: 737px; bottom: 0; }
  .why { position: absolute; left: 150px; top: 20px; right: 10px; }
  .why h2 { font-family: var(--heading-font); font-weight: 400; font-size: 25px; line-height: 1.12; }
  .why ul { list-style: none; margin-top: 10px; }
  .why li { font-family: var(--heading-font); font-size: 22px; color: var(--accent); line-height: 35.5px; }

  .tagline { position: absolute; left: 0; right: 0; top: 346px; text-align: center; font-family: var(--heading-font); font-size: 22px; line-height: 1.2; }
  .process { position: absolute; left: 18px; right: 18px; top: 417px; }
  .process .service-head h3 { font-size: 22px; }
  .steps { list-style: none; margin-top: 20px; font-size: 15px; line-height: 25.5px; }
  .steps li { padding-left: 14px; text-indent: -14px; }
  .steps li::before { content: "-"; display: inline-block; width: 14px; text-indent: 0; }

  /* Panel 3 */
  .panel--more .band--top { top: 0; left: 0; right: 0; height: 106px; }
  .panel--more .band--foot { left: 0; right: 0; top: 812px; bottom: 0; }
  .more-col { position: absolute; left: 22px; right: 22px; top: 130px; }
  .more-col .service { margin-top: 18px; }
  .more-col .service p { margin-top: 14px; }
  .more-col .service + .service { margin-top: 24px; }
  .pipe-list { font-size: 15.5px; line-height: 1.05; margin-top: 14px; text-align: justify; }

  .why-us { position: absolute; left: 20px; right: 20px; top: 826px; color: #fff; }
  .why-us h4 { font-family: var(--heading-font); font-weight: 400; font-size: 19px; color: #e7f3fb; }
  .why-us .traits { display: flex; justify-content: space-around; font-family: var(--heading-font); font-size: 19px; color: var(--ink); margin-top: 6px; }
</style>
</head>
<body>
<svg width="0" height="0" style="position:absolute" aria-hidden="true">
  <defs>
    <symbol id="arrow-badge" viewBox="0 0 28 28">
      <circle cx="14" cy="14" r="13" fill="#2a9ed8"/>
      <path d="M9 8 L21 14 L9 20 L12 14 Z" fill="#fff"/>
    </symbol>
    <symbol id="process-badge" viewBox="0 0 28 28">
      <rect x="1" y="1" width="26" height="26" rx="6" fill="#2a9ed8"/>
      <rect x="7" y="7" width="14" height="14" rx="2" fill="none" stroke="#fff" stroke-width="2"/>
      <path d="M14 10 V18 M10 14 H18" stroke="#fff" stroke-width="2"/>
    </symbol>
  </defs>
</svg>

<main class="brochure">
  <section class="panel panel--services">
    <div class="photo" role="img" aria-label="Photo of a calculator, pen and financial chart printout in cool blue tones"></div>
    <div class="band"></div>
    <div class="services-col">
      <h2 class="panel-title">Services</h2>
      <div class="service">
        <div class="service-head"><svg class="service-icon"><use href="#arrow-badge"/></svg><h3>Full Charge Bookkeeping</h3></div>
        <p>We can manage all aspects of your bookkeeping and business financials and communicate to you as much and as often as you want.</p>
      </div>
      <div class="service">
        <div class="service-head"><svg class="service-icon"><use href="#arrow-badge"/></svg><h3>Cash Management (Bill Pay &amp; Invoicing) &amp; Vendor Management</h3></div>
        <p>We can handle every step from receiving bills, communicating with vendor and paying bills. We take a lot pride in helping our clients save money and one way is negotiating with vendors and finding appropriate discounts.</p>
      </div>
      <div class="service">
        <div class="service-head"><svg class="service-icon"><use href="#arrow-badge"/></svg><h3>Financial Statements</h3></div>
        <p style="text-align:left">Profit and Loss – Balance Sheet – Statement of Cash Flow – Industry Specific</p>
        <p style="margin-top:0">We accurately prepare monthly, quarterly &amp; annual financial statements in a timely manner. We also take the time to review these statements with you so that you understand the financial health of your business.</p>
      </div>
    </div>
  </section>

  <section class="panel panel--why">
    <div class="photo" role="img" aria-label="Continuation of the financial chart photo"></div>
    <div class="band band--under-photo"></div>
    <div class="why">
      <h2>Why Outsource Bookkeeping?</h2>
      <ul>
        <li>Save Time</li>
        <li>Save Money</li>
        <li>Expertise</li>
        <li>Focused Staff</li>
        <li>Technology</li>
        <li>Experience</li>
      </ul>
    </div>
    <p class="tagline">The Financial Numbers are the<br>Heart Beat of an organization</p>
    <div class="process">
      <div class="service-head"><svg class="service-icon"><use href="#process-badge"/></svg><h3>The Process</h3></div>
      <ul class="steps">
        <li>Contact Us – we like to hear from you</li>
        <li>No-Obligation Consultation</li>
        <li>Review Current Process – identify strengths and weaknesses</li>
        <li>Recommend and implement new bookkeeping process</li>
        <li>Ongoing bookkeeping partnership</li>
        <li>Provide your company with more value and service to keep earning your business (ongoing)</li>
      </ul>
    </div>
    <div class="band band--foot"></div>
  </section>

  <section class="panel panel--more">
    <div class="band band--top"></div>
    <div class="more-col">
      <h2 class="panel-title">Services <small>(continued)</small></h2>
      <div class="service">
        <div class="service-head"><svg class="service-icon"><use href="#arrow-badge"/></svg><h3>Account Reconciliations</h3></div>
        <p>From bank account to credit card statements to vendor statements. We reconcile all of your accounts that impact your finances.</p>
      </div>
      <div class="service">
        <div class="service-head"><svg class="service-icon"><use href="#arrow-badge"/></svg><h3>Professional liaison</h3></div>
        <p>We will work directly with your other business partners – Bankers, CPA, Insurance, Payroll, Attorney... Need a loan? We will work directly with your banker to make the process as simple as possible. Does your CPA need some data? Let us take care of that while you continue making your customers happy.</p>
      </div>
      <div class="service">
        <div class="service-head"><svg class="service-icon"><use href="#arrow-badge"/></svg><h3>Business Services</h3></div>
        <p class="pipe-list">Create Proper Financial Systems | Projections Customized Reporting | Protection Planning Benchmarking | Online Filing Cabinet (Paperless)</p>
      </div>
      <div class="service">
        <div class="service-head"><svg class="service-icon"><use href="#arrow-badge"/></svg><h3>Exit/Succession Planning</h3></div>
        <p>We help you prepare your business for the next transition – planned (retirement) or unplanned (health). You’ve sacrificed to build this business (asset) we can help you transition it in the most efficient and valuable way.</p>
      </div>
    </div>
    <div class="band band--foot"></div>
    <div class="why-us">
      <h4>Why work with Halvick Ledgers?</h4>
      <div class="traits"><span>Proactive</span><span>Professional</span></div>
    </div>
  </section>
</main>
</body>
</html>
```